HR Technology Company (Corvexa) needs a consistent powerpoint deck for future presentations

We are Corvexa (corvexa-example.com). You can visit our website for colours scheme etc. I am looking for a full PPT pack which can be used for various presentations in the future. Sales Presentation, Company Overview etc. This must include charts, graphs, services (4/6/8 items), people slide, timeline slides etc among all the other common slides.

```html
<!DOCTYPE html>
<html lang="en">
<head>
<meta charset="utf-8">
<title>Corvexa – Presentation Deck Overview</title>
<link href="https://fonts.googleapis.com/css2?family=Outfit:wght@300;400;500;600;700&family=Poppins:wght@300;400;500;600&display=swap" rel="stylesheet">
<style>
  :root{
    --orange:#FFA50F;
    --orange-soft:#FFC56A;
    --yellow:#FFC93C;
    --blue:#5BA3F5;
    --blue-soft:#8DB8EC;
    --ink:#0B0B0B;
    --text:#1C1C1C;
    --muted:#8A8A8A;
    --track:#F2F2F2;
    --page:#E8E9EB;
    --panel:#F3F5FA;
    --white:#FFFFFF;
  }
  *{box-sizing:border-box;margin:0;padding:0}
  html,body{width:821px;height:1200px;overflow:hidden}
  body{background:var(--page);font-family:"Poppins",sans-serif;color:var(--text);position:relative}
  .slide{position:absolute;width:340px;height:191px;overflow:hidden;background:var(--white)}
  .slide > *{position:absolute}
  .col-l{left:55px}.col-r{left:425px}
  .row-1{top:55px}.row-2{top:276px}.row-3{top:497px}.row-4{top:718px}.row-5{top:938px}
  .dark{background:var(--ink);color:var(--white)}
  .rail{left:20px;top:0;width:0.6px;height:191px;background:#E6E6E6}
  .dark .rail{background:#2A2A2A}
  .rail-accent{left:20px;width:1.4px;background:var(--orange)}
  .dark .rail-accent{background:var(--white)}
  .pgnum{left:8px;top:12px;font-size:3.5px;color:var(--muted)}
  .eyebrow{left:31px;top:11px;font-size:5.5px;font-weight:400;display:flex;align-items:center;gap:4px}
  .eyebrow::after{content:"";width:8px;height:0.6px;background:var(--orange)}
  .brand{left:2px;top:169px;width:18px;text-align:center;font-family:"Outfit",sans-serif;font-weight:600;font-size:4.6px;color:var(--orange)}
  .title{left:31px;top:24px;font-family:"Outfit",sans-serif;font-weight:600;font-size:16.5px;line-height:1;color:var(--ink);white-space:nowrap}
  .dark .title{color:var(--white)}
  .title em{font-style:normal;color:var(--orange)}
  .site{font-size:4.2px}
  .tiny{font-size:3.6px;line-height:1.45;color:#555}
  svg{display:block}

  /* Why us */
  .why-title{left:31px;top:75px;font-family:"Outfit",sans-serif;font-weight:600;font-size:16px;line-height:0.95}
  .pill{background:var(--white);color:var(--ink);border-radius:19px;width:137px;height:37px;padding:10px 0 0 15px}
  .pill h4{font-family:"Outfit",sans-serif;font-size:5.6px;font-weight:600}
  .pill p{font-size:3.3px;line-height:1.5;color:#888;margin-top:2px;width:88px}
  .num{width:18px;height:18px;border-radius:50%;background:var(--orange);color:var(--white);font-family:"Outfit",sans-serif;font-weight:600;font-size:6px;display:flex;align-items:center;justify-content:center;border:1.5px solid #1a1a1a}

  /* Market analysis */
  .orange-panel{left:0;top:0;width:120px;height:191px;background:var(--orange)}
  .bar{height:25px;width:157px;background:var(--track);border-radius:1px}
  .bar .fill{position:absolute;left:0;top:0;height:25px;color:var(--white);padding:5px 0 0 22px;font-family:"Outfit",sans-serif}
  .bar .fill b{font-size:6px;font-weight:600;display:block}
  .bar .fill span{font-size:3.2px;opacity:.9}
  .bar .fill svg{position:absolute;left:6px;top:7px}

  /* Audience */
  .warm{background:linear-gradient(135deg,#FCEBD7 0%,#FDF4EA 55%,#FBF7F2 100%)}
  .headline{font-family:"Outfit",sans-serif;font-weight:600;font-size:11px;line-height:1.14;color:var(--ink)}
  .card{left:151px;width:164px;height:58px;border-radius:7px;padding:8px 0 0 11px}
  .card h5{font-size:6.2px;font-weight:400}
  .card .people{position:absolute;left:9px;top:26px;display:flex;gap:5px}
  .card .gauge{position:absolute;right:14px;top:16px}

  /* Funds */
  .table{left:35px;top:52px;width:280px;border-top:0.5px solid #444;border-collapse:collapse;font-size:4px}
  .table th{color:var(--orange);font-weight:400;text-align:left;height:16px;font-size:4.6px;border-bottom:0.5px solid #444}
  .table td{height:12.2px;color:#DDD}
  .table tr:first-child td{padding-top:4px}
  .table tr.last td{border-bottom:0.5px solid #444;padding-bottom:2px}
  .fund-pill{left:36px;top:146px;width:279px;height:37px;border-radius:19px;background:var(--white);color:var(--ink)}
  .fund-pill .stat{position:absolute;top:9px;text-align:center}
  .fund-pill small{display:block;font-size:3.6px;color:#666;letter-spacing:.1px}
  .fund-pill strong{display:block;font-family:"Outfit",sans-serif;font-weight:600;font-size:9px;color:var(--orange);margin-top:1px}

  /* Testimonial */
  .quote-mark{left:30px;top:42px;font-family:"Outfit",sans-serif;font-weight:700;font-size:30px;line-height:1;color:var(--orange)}
  .quote{left:33px;top:64px;font-family:"Outfit",sans-serif;font-weight:300;font-size:9.6px;line-height:1.16;color:var(--ink)}
  .who{left:33px;top:121px;font-family:"Outfit",sans-serif;font-weight:600;font-size:6.2px;color:var(--orange)}
  .role{left:33px;top:131px;font-size:4px;color:var(--muted)}

  /* Projections */
  .tag{font-size:4.6px;padding:1.5px 4px;color:var(--white);border-radius:1px;white-space:nowrap}
  .tag.o{background:var(--orange)}.tag.k{background:var(--ink)}
  .yr{font-size:4.6px;color:var(--ink)}
  .kpi{top:133px;width:64px;height:36px;border:0.6px dashed var(--orange-soft);border-radius:3px;padding:7px 0 0 8px}
  .kpi b{display:block;font-family:"Outfit",sans-serif;font-size:13px;font-weight:600;line-height:1}
  .kpi span{font-size:4.2px;color:#777}

  /* Targets */
  .side-panel{left:0;top:0;width:148px;height:191px;background:var(--panel)}
  .tgt-title{left:31px;top:25px;font-family:"Outfit",sans-serif;font-weight:600;font-size:16.5px;line-height:0.98;color:var(--ink)}
  .tgt-title em{font-style:normal;color:var(--orange)}
  .tgt-copy{left:31px;top:67px;width:90px}
  .tgt-item{left:189px;width:122px;height:43px}
  .tgt-item .ic{position:absolute;left:0;top:2px;width:25px;height:25px;border-radius:50%;background:#FFF5E6;display:flex;align-items:center;justify-content:center}
  .tgt-item b{position:absolute;left:34px;top:6px;font-family:"Outfit",sans-serif;font-size:7.2px;font-weight:600;color:var(--ink);white-space:nowrap}
  .tgt-item span{position:absolute;left:34px;top:16px;font-size:3.6px;color:#555}
  .tgt-item::after{content:"";position:absolute;left:0;right:0;bottom:0;height:0.5px;background:#E5E5E5}

  /* Milestones */
  .ms-text b{display:block;font-family:"Outfit",sans-serif;font-size:6.3px;font-weight:600;color:var(--ink)}
  .ms-text p{margin-top:3px;width:60px}
  .month{font-size:3.6px;padding:1px 3px;color:var(--white);text-transform:uppercase}
  .goal{text-align:center;width:46px}
  .goal b{display:block;font-family:"Outfit",sans-serif;font-size:5.6px;font-weight:600;color:var(--ink)}
  .goal p{font-size:3.6px;color:#555;line-height:1.5;margin-top:2px}
</style>
</head>
<body>

<!-- 1. Why us -->
<section class="slide dark col-l row-1">
  <svg style="left:0;top:0" width="340" height="191" viewBox="0 0 340 191">
    <defs><radialGradient id="globe" cx="0.35" cy="0.35" r="0.7"><stop offset="0" stop-color="#6a6a6a"/><stop offset="0.7" stop-color="#1c1c1c"/><stop offset="1" stop-color="#0b0b0b"/></radialGradient></defs>
    <circle cx="280" cy="140" r="52" fill="url(#globe)"/>
    <circle cx="102" cy="95" r="88" fill="none" stroke="#161616" stroke-width="14"/>
    <path d="M27 50 A70 70 0 1 1 56 167" fill="none" stroke="var(--orange)" stroke-width="0.6" stroke-dasharray="1.6 1.6"/>
    <circle cx="27" cy="50" r="1" fill="var(--orange)"/><circle cx="56" cy="167" r="1" fill="var(--orange)"/>
    <path d="M122 62 L145 45 M128 95 L160 95 M120 130 L145 146" stroke="var(--orange)" stroke-width="0.5" stroke-dasharray="1.4 1.4"/>
  </svg>
  <div class="rail"></div><div class="rail-accent" style="top:75px;height:36px"></div>
  <span class="pgnum">8</span>
  <span class="eyebrow">About Markets</span>
  <h2 class="why-title">Why<br>Us?</h2>
  <div class="pill" style="left:149px;top:18px"><h4>Growth Hacks</h4><p>Track live, useful insight into staff performance across the whole company.</p>
    <svg style="position:absolute;right:10px;top:10px" width="17" height="17" viewBox="0 0 17 17" fill="none" stroke="var(--orange)" stroke-width="0.7"><rect x="1" y="8" width="8" height="8"/><circle cx="12" cy="11" r="4"/><path d="M8 7V3M8 3l-2 -1M8 3l2 -1"/></svg></div>
  <div class="pill" style="left:170px;top:77px"><h4>Boost Business</h4><p>Track live, useful insight into staff performance across the whole company.</p>
    <svg style="position:absolute;right:10px;top:10px" width="17" height="17" viewBox="0 0 17 17" fill="none" stroke="var(--orange)" stroke-width="0.7"><rect x="1" y="2" width="15" height="10"/><path d="M4 10V7M7 10V5M10 10V6M13 10V4M6 15h5M8.5 12v3"/></svg></div>
  <div class="pill" style="left:149px;top:135px"><h4>Go Global</h4><p>Track live, useful insight into staff performance across the whole company.</p>
    <svg style="position:absolute;right:10px;top:10px" width="17" height="17" viewBox="0 0 17 17" fill="none" stroke="var(--orange)" stroke-width="0.7"><circle cx="8" cy="9" r="7"/><ellipse cx="8" cy="9" rx="3" ry="7"/><path d="M1 9h14M2 5h12M2 13h12"/></svg></div>
  <div class="num" style="left:139px;top:27px">01</div>
  <div class="num" style="left:160px;top:86px">02</div>
  <div class="num" style="left:139px;top:144px">03</div>
  <span class="brand">Corvexa</span>
</section>

<!-- 2. Market analysis -->
<section class="slide col-r row-1">
  <div class="orange-panel"></div>
  <svg style="left:0;top:0" width="340" height="191" viewBox="0 0 340 191"><path d="M323 22 A60 60 0 0 0 270 72 A60 60 0 0 0 340 114" fill="none" stroke="var(--orange-soft)" stroke-width="0.5" stroke-dasharray="1.5 1.5"/></svg>
  <span class="pgnum" style="color:#fff">15</span>
  <span class="eyebrow" style="color:#fff">Market Size</span>
  <div style="left:119px;top:26px;width:1.4px;height:18px;background:var(--ink)"></div>
  <h2 class="title" style="left:129px">Market <em>Analysis</em></h2>
  <div class="bar" style="left:97px;top:54px"><div class="fill" style="width:55px;background:var(--orange)"><svg width="12" height="12" viewBox="0 0 12 12" fill="none" stroke="#fff" stroke-width="0.7"><circle cx="6" cy="6" r="2"/><circle cx="2" cy="2" r="1"/><circle cx="10" cy="2" r="1"/><circle cx="2" cy="10" r="1"/><circle cx="10" cy="10" r="1"/><path d="M3 3l1.5 1.5M9 3L7.5 4.5M3 9l1.5-1.5M9 9L7.5 7.5"/></svg><b>40%</b><span>Text Here</span></div></div>
  <div class="bar" style="left:127px;top:84px"><div class="fill" style="width:58px;background:var(--blue-soft)"><svg width="12" height="12" viewBox="0 0 12 12" fill="none" stroke="#fff" stroke-width="0.7"><rect x="1" y="2" width="7" height="5"/><path d="M3 10c2-2 4-2 8-1"/></svg><b>27%</b><span>Text Here</span></div></div>
  <div class="bar" style="left:106px;top:114px"><div class="fill" style="width:53px;background:var(--blue)"><svg width="12" height="12" viewBox="0 0 12 12" fill="none" stroke="#fff" stroke-width="0.7"><rect x="1" y="3" width="9" height="7"/><path d="M4 3V1.5h3V3"/><circle cx="10" cy="9" r="2"/></svg><b>23%</b><span>Text Here</span></div></div>
  <div class="bar" style="left:159px;top:143px"><div class="fill" style="width:56px;background:var(--yellow)"><svg width="12" height="12" viewBox="0 0 12 12" fill="none" stroke="#fff" stroke-width="0.7"><path d="M2 10c0-3 2-5 4-5s4 2 4 5z"/><circle cx="8" cy="3" r="2"/></svg><b>20%</b><span>Text Here</span></div></div>
  <span class="site" style="left:31px;top:176px;color:#fff">corvexa-example.com</span>
</section>

<!-- 3. Audience -->
<section class="slide warm col-l row-2">
  <svg width="0" height="0" style="position:absolute"><defs>
    <symbol id="user" viewBox="0 0 16 18"><circle cx="8" cy="5" r="4" fill="none" stroke-width="1.6"/><path d="M1 18c0-5 3-7 7-7s7 2 7 7" fill="none" stroke-width="1.6"/></symbol>
  </defs></svg>
  <span class="pgnum">19</span>
  <span class="eyebrow">Market Size</span>
  <div class="rail-accent" style="top:62px;height:68px"></div>
  <h2 class="headline" style="left:31px;top:65px">Bring<br>workforce<br>performance<br>to the next<br>level</h2>
  <div class="card" style="top:34px;background:var(--orange);color:var(--ink)"><h5>Our Audience</h5>
    <div class="people">
      <svg width="16" height="18" stroke="#fff"><use href="#user"/></svg><svg width="16" height="18" stroke="#fff"><use href="#user"/></svg><svg width="16" height="18" stroke="#fff"><use href="#user"/></svg><svg width="16" height="18" stroke="#FFC56A"><use href="#user"/></svg><svg width="16" height="18" stroke="#FFC56A"><use href="#user"/></svg>
    </div>
    <svg class="gauge" width="28" height="28" viewBox="0 0 28 28"><circle cx="14" cy="14" r="13" fill="#FFD08A"/><path d="M14 1 A13 13 0 1 1 2 19 L14 14Z" fill="#fff"/><circle cx="14" cy="14" r="10" fill="var(--ink)"/></svg>
  </div>
  <div class="card" style="top:99px;background:var(--ink);color:#fff"><h5>Retension Rate</h5>
    <div class="people">
      <svg width="16" height="18" stroke="#fff"><use href="#user"/></svg><svg width="16" height="18" stroke="#fff"><use href="#user"/></svg><svg width="16" height="18" stroke="#444"><use href="#user"/></svg><svg width="16" height="18" stroke="#444"><use href="#user"/></svg><svg width="16" height="18" stroke="#444"><use href="#user"/></svg>
    </div>
    <svg class="gauge" width="28" height="28" viewBox="0 0 28 28"><circle cx="14" cy="14" r="13" fill="#fff"/><path d="M14 1 A13 13 0 0 1 21.6 24.5 L14 14Z" fill="var(--orange)"/><circle cx="14" cy="14" r="10" fill="var(--orange)"/><text x="14" y="15.6" font-size="5" font-family="Outfit,sans-serif" font-weight="600" text-anchor="middle" fill="#111">40%</text></svg>
  </div>
  <span class="brand">Corvexa</span>
</section>

<!-- 4. Overview of funds -->
<section class="slide dark col-r row-2">
  <div class="rail"></div><div class="rail-accent" style="top:27px;height:16px"></div>
  <span class="pgnum">39</span>
  <span class="eyebrow">Financial</span>
  <h2 class="title">Overview of <em>Funds</em></h2>
  <table class="table">
    <tr><th style="padding-left:6px;width:130px">Financial Type</th><th style="width:49px">2021</th><th style="width:49px">2022</th><th>2023</th></tr>
    <tr><td style="padding-left:6px">Average Monthly Active User</td><td>30,000</td><td>50,000</td><td>170,000</td></tr>
    <tr><td style="padding-left:6px">Average Growth</td><td>1.7%</td><td>8.4%</td><td>20.2%</td></tr>
    <tr><td style="padding-left:6px">Market Penetration</td><td>2%</td><td>4%</td><td>9%</td></tr>
    <tr><td style="padding-left:6px">Revenue</td><td>100,000</td><td>4,000,000</td><td>130,000,000</td></tr>
    <tr class="last"><td style="padding-left:6px">Profits</td><td>310,000</td><td>3,000,000</td><td>27,000,000</td></tr>
  </table>
  <div class="fund-pill">
    <div class="stat" style="left:19px;text-align:left"><small>Average</small><strong>2 Years</strong></div>
    <svg style="position:absolute;left:74px;top:14px" width="10" height="8" viewBox="0 0 10 8"><path d="M1 1l3 3-3 3M5 1l3 3-3 3" fill="none" stroke="var(--orange-soft)" stroke-width="1.2"/></svg>
    <div class="stat" style="left:105px"><small>PROFIT</small><strong>25%</strong></div>
    <div class="stat" style="left:154px"><small>NET INCOME</small><strong>$3.6m</strong></div>
    <div class="stat" style="left:216px"><small>RATE</small><strong>Stocks</strong></div>
  </div>
</section>

<!-- 5. Testimonial -->
<section class="slide col-l row-3">
  <svg style="left:0;top:0" width="340" height="191" viewBox="0 0 340 191">
    <defs><linearGradient id="ring" x1="0" y1="0" x2="1" y2="1"><stop offset="0" stop-color="#FFA50F"/><stop offset="1" stop-color="#FFE3B5"/></linearGradient>
    <linearGradient id="meeting" x1="0" y1="0" x2="1" y2="1"><stop offset="0" stop-color="#c9ccd2"/><stop offset="0.5" stop-color="#4c5564"/><stop offset="1" stop-color="#2a2f38"/></linearGradient></defs>
    <circle cx="257" cy="96" r="113" fill="none" stroke="#FFE0B0" stroke-width="0.5" stroke-dasharray="1.5 1.5"/>
    <circle cx="257" cy="96" r="75" fill="none" stroke="#F6F0E6" stroke-width="0.5"/>
    <circle cx="257" cy="96" r="55" fill="url(#ring)"/>
    <circle cx="257" cy="96" r="45" fill="url(#meeting)" role="img" aria-label="Photo of two business people reviewing a tablet in an office"/>
  </svg>
  <div class="rail"></div>
  <span class="pgnum">23</span>
  <span class="eyebrow">Testimonials</span>
  <span class="quote-mark">“</span>
  <p class="quote">We're Helping Hundreds<br>of Organisations<br>Transform Their<br>HR Function</p>
  <span class="who">Dana Whitlow</span>
  <span class="role">CEO</span>
  <span class="brand">Corvexa</span>
</section>

<!-- 6. Financial projections -->
<section class="slide col-r row-3">
  <svg style="left:0;top:0" width="340" height="191" viewBox="0 0 340 191">
    <defs><radialGradient id="rev" cx="0.5" cy="0.4" r="0.6"><stop offset="0" stop-color="#FFC56A"/><stop offset="1" stop-color="#FFE6C0"/></radialGradient></defs>
    <circle cx="62" cy="102" r="21" fill="none" stroke="var(--orange-soft)" stroke-width="0.5" stroke-dasharray="1.2 1.2"/>
    <circle cx="62" cy="102" r="17" fill="url(#rev)"/>
    <text x="62" y="103" font-family="Outfit,sans-serif" font-weight="600" font-size="7.5" fill="#fff" text-anchor="middle">$12m</text>
    <text x="62" y="109" font-family="Poppins,sans-serif" font-size="3.2" fill="#fff" text-anchor="middle">Revenue</text>
    <path d="M115 104 L171 94 L220 83 Q250 72 277 59" fill="none" stroke="var(--orange)" stroke-width="0.5" stroke-dasharray="1.5 1"/>
    <circle cx="115" cy="104" r="2.4" fill="var(--orange)"/><circle cx="171" cy="94" r="2.4" fill="var(--orange)"/>
    <circle cx="220" cy="83" r="2.4" fill="var(--orange)"/><circle cx="277" cy="59" r="2.4" fill="var(--orange)"/>
  </svg>
  <div class="rail"></div><div class="rail-accent" style="top:27px;height:16px"></div>
  <span class="pgnum">40</span>
  <span class="eyebrow">Financial</span>
  <h2 class="title">Financial <em>Projections</em></h2>
  <p class="tiny" style="left:31px;top:52px;width:100px;font-size:4.2px;color:#333">Our financial forecasts are ahead of what our rivals can show</p>
  <span class="yr" style="left:108px;top:71px">2018</span><span class="tag o" style="left:97px;top:79px">$800,000</span>
  <span class="yr" style="left:164px;top:61px">2019</span><span class="tag o" style="left:149px;top:69px">$1,800,000</span>
  <span class="yr" style="left:213px;top:50px">2020</span><span class="tag k" style="left:197px;top:60px">$3,800,000</span>
  <span class="yr" style="left:271px;top:31px">2021</span><span class="tag k" style="left:257px;top:41px">$5,590,000</span>
  <div class="kpi" style="left:33px"><b>1m</b><span>Text here</span></div>
  <div class="kpi" style="left:105px"><b>50%</b><span>Text here</span></div>
  <div class="kpi" style="left:177px"><b>29k</b><span>Text here</span></div>
  <div class="kpi" style="left:249px"><b>500</b><span>Text here</span></div>
  <span class="brand">Corvexa</span>
</section>

<!-- 7. Financial targets with list -->
<section class="slide col-l row-4">
  <div class="side-panel"></div>
  <div class="rail"></div><div class="rail-accent" style="top:26px;height:16px"></div>
  <span class="pgnum">42</span>
  <span class="eyebrow">Fundraising</span>
  <h2 class="tgt-title">Financial<br><em>Targets</em></h2>
  <p class="tiny tgt-copy">Corvexa is a leading workforce change partner - our strength lies in deep Nimbus HR Suite skill, a clear grasp of your business needs and a steady drive for your success. We do our best work when we innovate - our tailored services are an asset that go beyond the obvious to meet your business needs and grow your Nimbus HR Suite setup.</p>
  <div style="left:102px;top:116px;width:62px;height:70px;border-radius:4px;background:linear-gradient(160deg,#EDEFF5,#D9DCE6 60%,#FFD08A)" role="img" aria-label="Illustration of people analysing charts on a stack of reports"></div>
  <span class="site" style="left:31px;top:174px">corvexa-example.com</span>
  <div class="tgt-item" style="top:12px"><div class="ic"><svg width="12" height="12" viewBox="0 0 12 12" fill="none" stroke="var(--orange)" stroke-width="0.7"><path d="M1 7l3-3 2 1 2-2 3 3-4 4z"/></svg></div><b>$45.8 million</b><span>Insert Subtitle Here</span></div>
  <div class="tgt-item" style="top:55px"><div class="ic"><svg width="12" height="12" viewBox="0 0 12 12" fill="none" stroke="var(--orange)" stroke-width="0.7"><circle cx="6" cy="6" r="5"/><circle cx="6" cy="6" r="3"/><circle cx="6" cy="6" r="1"/></svg></div><b>$15.8 million</b><span>Insert Subtitle Here</span></div>
  <div class="tgt-item" style="top:98px"><div class="ic"><svg width="12" height="12" viewBox="0 0 12 12" fill="none" stroke="var(--orange)" stroke-width="0.7"><path d="M6 1l4 2v3c0 3-2 4-4 5-2-1-4-2-4-5V3z"/></svg></div><b>$45.8 million</b><span>Insert Subtitle Here</span></div>
  <div class="tgt-item" style="top:141px"><div class="ic"><svg width="12" height="12" viewBox="0 0 12 12" fill="none" stroke="var(--orange)" stroke-width="0.7"><circle cx="6" cy="4" r="3"/><path d="M1 10h3l2 1 4-2"/></svg></div><b>40 percent</b><span>Insert Subtitle Here</span></div>
  <span class="brand">Corvexa</span>
</section>

<!-- 8. Financial targets with photo -->
<section class="slide col-r row-4">
  <div class="side-panel" style="width:149px"></div>
  <div class="rail"></div><div class="rail-accent" style="top:26px;height:16px"></div>
  <span class="pgnum">43</span>
  <span class="eyebrow">Fundraising</span>
  <h2 class="tgt-title">Financial<br><em>Targets</em></h2>
  <p class="tiny" style="left:31px;top:71px;width:104px">Corvexa is a leading workforce change partner - our strength lies in deep Nimbus HR Suite skill, a clear grasp of your business needs and a steady drive for your success. We do our best work when we innovate - our tailored services are an asset that go beyond the obvious to meet your business needs and grow your Nimbus HR Suite setup.</p>
  <span class="site" style="left:31px;top:174px">corvexa-example.com</span>
  <div style="left:149px;top:0;width:191px;height:191px;background:linear-gradient(135deg,#2E3B52 0%,#6C7C96 45%,#C9D2E0 75%,#7D8BA3 100%)" role="img" aria-label="Photo of hands using a tablet showing bar charts over printed reports"></div>
  <span class="brand">Corvexa</span>
</section>

<!-- 9. Milestone line -->
<section class="slide col-l row-5">
  <svg style="left:0;top:0" width="340" height="191" viewBox="0 0 340 191">
    <line x1="20" y1="106" x2="340" y2="106" stroke="var(--orange)" stroke-width="0.6"/>
    <path d="M89 60V103M200 60V103M34 113V162M145 113V162M254 113V162" stroke="var(--orange)" stroke-width="0.5"/>
    <g>
      <circle cx="62" cy="106" r="14" fill="#fff"/><circle cx="62" cy="106" r="12" fill="var(--orange)"/>
      <circle cx="116" cy="106" r="14" fill="#fff"/><circle cx="116" cy="106" r="12" fill="var(--ink)"/>
      <circle cx="171" cy="106" r="14" fill="#fff"/><circle cx="171" cy="106" r="12" fill="var(--orange)"/>
      <circle cx="226" cy="106" r="14" fill="#fff"/><circle cx="226" cy="106" r="12" fill="var(--ink)"/>
      <circle cx="280" cy="106" r="14" fill="#fff"/><circle cx="280" cy="106" r="12" fill="var(--orange)"/>
    </g>
    <g fill="none" stroke="#fff" stroke-width="0.6">
      <path d="M57 109h10M59 109v-4h6v4M62 101v3"/>
      <circle cx="116" cy="106" r="2"/><path d="M112 102l2 2M120 102l-2 2M112 110l2-2M120 110l-2-2"/>
      <path d="M166 108l3-3 2 1 2-2 3 3-4 4z"/>
      <rect x="221" y="102" width="9" height="7"/><path d="M224 102v-1.5h3v1.5"/>
      <path d="M276 110v-3M279 110v-5M282 110v-4M285 110v-6"/>
    </g>
  </svg>
  <div class="rail"></div><div class="rail-accent" style="top:27px;height:16px"></div>
  <span class="pgnum">35</span>
  <span class="eyebrow">Milestone</span>
  <h2 class="title">The <em>Milestone</em></h2>
  <span class="month" style="left:20px;top:113px;background:var(--orange)">January</span>
  <span class="month" style="left:77px;top:98px;background:var(--orange)">February</span>
  <span class="month" style="left:133px;top:113px;background:var(--ink)">March</span>
  <span class="month" style="left:192px;top:98px;background:var(--orange)">April</span>
  <span class="month" style="left:244px;top:113px;background:var(--ink)">May</span>
  <div class="ms-text" style="left:95px;top:57px"><b>Insert Title</b><p class="tiny">HR metrics are key measures used to gauge the value and impact</p></div>
  <div class="ms-text" style="left:206px;top:57px"><b>Insert Title</b><p class="tiny">HR metrics are key measures used to gauge the value and impact</p></div>
  <div class="ms-text" style="left:40px;top:130px"><b>Insert Title</b><p class="tiny">HR metrics are key measures used to gauge the value and impact</p></div>
  <div class="ms-text" style="left:151px;top:130px"><b>Insert Title</b><p class="tiny">HR metrics are key measures used to gauge the value and impact</p></div>
  <div class="ms-text" style="left:260px;top:130px"><b>Insert Title</b><p class="tiny">HR metrics are key measures used to gauge the value and impact</p></div>
  <span class="brand">Corvexa</span>
</section>

<!-- 10. Timeline rings -->
<section class="slide col-r row-5">
  <svg style="left:0;top:0" width="340" height="191" viewBox="0 0 340 191" font-family="Outfit,sans-serif">
    <g fill="none" stroke-width="2.6">
      <circle cx="56" cy="87" r="23" stroke="#F1F1F1"/><path d="M33 87 A23 23 0 0 1 79 87" stroke="var(--orange)"/>
      <circle cx="102" cy="87" r="23" stroke="#F1F1F1"/><path d="M79 87 A23 23 0 0 0 125 87" stroke="var(--orange)"/>
      <circle cx="147" cy="87" r="23" stroke="#F1F1F1"/><path d="M124 87 A23 23 0 0 1 170 87" stroke="var(--orange)"/>
      <circle cx="193" cy="87" r="23" stroke="#F1F1F1"/><path d="M170 87 A23 23 0 0 0 216 87" stroke="var(--orange)"/>
      <circle cx="239" cy="87" r="23" stroke="#F1F1F1"/><path d="M216 87 A23 23 0 0 1 262 87" stroke="var(--orange)"/>
      <circle cx="285" cy="87" r="23" stroke="#F1F1F1"/><path d="M262 87 A23 23 0 0 0 308 87" stroke="var(--orange)"/>
    </g>
    <g font-size="8" font-weight="600" fill="var(--orange)" text-anchor="middle">
      <text x="56" y="88">2021</text><text x="102" y="88">2022</text><text x="147" y="88">2023</text><text x="193" y="88">2024</text><text x="239" y="88">2025</text><text x="285" y="88">2026</text>
    </g>
    <g font-size="4.2" fill="#333" text-anchor="middle" font-family="Poppins,sans-serif">
      <text x="56" y="95">Goal</text><text x="102" y="95">Goal</text><text x="147" y="95">Goal</text><text x="193" y="95">Goal</text><text x="239" y="95">Goal</text><text x="285" y="95">Goal</text>
    </g>
    <g fill="none" stroke="var(--orange)" stroke-width="1.3">
      <path d="M53 117l3 3 3-3M53 121l3 3 3-3"/><path d="M99 117l3 3 3-3M99 121l3 3 3-3"/><path d="M144 117l3 3 3-3M144 121l3 3 3-3"/>
      <path d="M190 117l3 3 3-3M190 121l3 3 3-3"/><path d="M236 117l3 3 3-3M236 121l3 3 3-3"/><path d="M282 117l3 3 3-3M282 121l3 3 3-3"/>
    </g>
  </svg>
  <div class="rail"></div><div class="rail-accent" style="top:27px;height:16px;background:var(--ink)"></div>
  <span class="pgnum">37</span>
  <span class="eyebrow">Timeline</span>
  <h2 class="title">The <em>Milestone</em></h2>
  <div class="goal" style="left:33px;top:133px"><b>Insert Title</b><p>Text here please.<br>Text here</p></div>
  <div class="goal" style="left:79px;top:133px"><b>Insert Title</b><p>Text here please.<br>Text here</p></div>
  <div class="goal" style="left:124px;top:133px"><b>Insert Title</b><p>Text here please.<br>Text here</p></div>
  <div class="goal" style="left:170px;top:133px"><b>Insert Title</b><p>Text here please.<br>Text here</p></div>
  <div class="goal" style="left:216px;top:133px"><b>Insert Title</b><p>Text here please.<br>Text here</p></div>
  <div class="goal" style="left:262px;top:133px"><b>Insert Title</b><p>Text here please.<br>Text here</p></div>
  <span class="brand">Corvexa</span>
</section>

</body>
</html>
```